A4 Menu needed for cafe - attached design

Need an A4 menu designed for our cafe.
I have attached our catering menu - I would like the new menu to be designed in the exact same way.

I have attached the text that needs to appear on the menu

Industry/Entity Type

Catering

```html
<!DOCTYPE html>
<html lang="en">
<head>
<meta charset="utf-8">
<title>Daily Remedy – Catering Menu</title>
<link href="https://fonts.googleapis.com/css2?family=Merriweather:wght@400&display=swap" rel="stylesheet">
<style>
  :root {
    --page: #e3c699;
    --board: #2a2526;
    --cream: #f5ec9c;
    --rule: #a9a06a;
    --ink: #f3f0e8;
    --frame: #d9d5c8;
    --ribbon-line: #c9c08a;
  }
  * { margin: 0; padding: 0; box-sizing: border-box; }
  html, body { width: 1200px; height: 900px; overflow: hidden; }
  body {
    background: var(--page);
    font-family: "Merriweather", Georgia, serif;
    position: relative;
  }
  .card {
    position: absolute;
    top: 44px;
    width: 574px;
    height: 405px;
    background: var(--board);
    color: var(--ink);
  }
  .card--back { left: 17px; }
  .card--front { left: 600px; border: 1px solid var(--rule); }

  .brand {
    position: absolute;
    left: 0; right: 0;
    display: flex;
    align-items: center;
    justify-content: center;
    gap: 8px;
    color: var(--cream);
    letter-spacing: 0.04em;
  }
  .brand__mark { background: var(--cream); display: block; }
  .card--back .brand { top: 60px; font-size: 18px; }
  .card--back .brand__mark { width: 18px; height: 18px; }
  .card--front .brand { top: 38px; font-size: 15px; }
  .card--front .brand__mark { width: 14px; height: 14px; }

  .rule { position: absolute; height: 1px; background: var(--rule); }
  .rule--upper { left: 90px; width: 406px; top: 158px; }
  .rule--lower { left: 53px; width: 481px; top: 262px; }

  .title {
    position: absolute;
    left: 0; right: 0;
    text-align: center;
    color: var(--cream);
    font-weight: 400;
  }
  .card--back .title { top: 180px; font-size: 40px; letter-spacing: 0.01em; }
  .card--front .title { top: 91px; font-size: 13.5px; }

  .section {
    position: absolute;
    border: 1px solid var(--frame);
    padding: 12px 8px 0;
  }
  .section--breakfast { left: 53px; top: 131px; width: 201px; height: 143px; }
  .section--lunch { left: 318px; top: 131px; width: 229px; height: 143px; padding-left: 15px; }
  .section--light { left: 138px; top: 296px; width: 288px; height: 103px; padding-top: 12px; display: flex; }

  .ribbon {
    position: absolute;
    top: -12px;
    width: 146px;
    height: 19px;
    left: 50%;
    transform: translateX(-50%);
  }
  .ribbon svg { position: absolute; inset: 0; }
  .ribbon__label {
    position: relative;
    display: block;
    text-align: center;
    font-size: 12px;
    line-height: 19px;
    letter-spacing: 0.02em;
    color: var(--ink);
    white-space: nowrap;
  }

  .items {
    list-style: none;
    font-size: 8px;
    line-height: 11.5px;
  }
  .items li { display: flex; }
  .items .name { white-space: nowrap; flex: none; }
  .items .price { white-space: nowrap; }
  .section--breakfast .name { width: 138px; }
  .section--lunch .name { width: 134px; }
  .items--left { width: 152px; flex: none; }
  .items--left .name { width: 108px; }
  .items--right .name { width: 103px; }
</style>
</head>
<body>

<section class="card card--back" aria-label="Menu back">
  <div class="brand"><span class="brand__mark"></span><span>Daily Remedy</span></div>
  <div class="rule rule--upper"></div>
  <h1 class="title">catering menu</h1>
  <div class="rule rule--lower"></div>
</section>

<section class="card card--front" aria-label="Menu front">
  <div class="brand"><span class="brand__mark"></span><span>Daily Remedy</span></div>
  <h2 class="title">catering menu</h2>

  <div class="section section--breakfast">
    <div class="ribbon">
      <svg viewBox="0 0 146 19" width="146" height="19"><polygon points="0,0 146,0 139,9.5 146,19 0,19 7,9.5" fill="#2a2526" stroke="#c9c08a" stroke-width="1"/></svg>
      <span class="ribbon__label">BREAKFAST</span>
    </div>
    <ul class="items">
      <li><span class="name">Toast</span><span class="price">$2 per slice</span></li>
      <li><span class="name">Raisin Toast</span><span class="price">$2 per slice</span></li>
      <li><span class="name">Egg Bacon and Cheese Roll</span><span class="price">$6.5</span></li>
      <li><span class="name">Veggie Brekky Wrap</span><span class="price">$6.5</span></li>
      <li><span class="name">Ham and Cheese French Toast</span><span class="price">$6.5</span></li>
      <li><span class="name">Ham and Cheese Toastie</span><span class="price">$5.5</span></li>
      <li><span class="name">Cheese and Tomato Toastie</span><span class="price">$5.5</span></li>
      <li><span class="name">Ham and Cheese Croissant</span><span class="price">$6.5</span></li>
      <li><span class="name">Cheese and tomato Croissant</span><span class="price">$6.0</span></li>
      <li><span class="name">Ham Cheese and Tomato Toastie</span><span class="price">$6.0</span></li>
      <li><span class="name">Plain Croissant</span><span class="price">$3.5</span></li>
    </ul>
  </div>

  <div class="section section--lunch">
    <div class="ribbon">
      <svg viewBox="0 0 146 19" width="146" height="19"><polygon points="0,0 146,0 139,9.5 146,19 0,19 7,9.5" fill="#2a2526" stroke="#c9c08a" stroke-width="1"/></svg>
      <span class="ribbon__label">LUNCH</span>
    </div>
    <ul class="items">
      <li><span class="name">Pre made Sandwiches</span><span class="price">$6.5/$7.5</span></li>
      <li><span class="name">Pre made Focaccias</span><span class="price">$8.5</span></li>
      <li><span class="name">Pre made Wraps</span><span class="price">$7.5</span></li>
      <li><span class="name">Pre made Mini Rolls</span><span class="price">$4.0</span></li>
      <li><span class="name">Pre made Baguettes</span><span class="price">$9.0</span></li>
      <li><span class="name">Pre made Bagels</span><span class="price">$9.0</span></li>
      <li><span class="name">Fresh Salads made daily</span><span class="price">$9.5</span></li>
      <li><span class="name">Hot Chips</span><span class="price">$4.5</span></li>
      <li><span class="name">Plain Hamburger</span><span class="price">$7.5</span></li>
      <li><span class="name">Hamburger with the Lot</span><span class="price">$9.0</span></li>
      <li><span class="name">Chicken Schnitzel Burger</span><span class="price">$8.5</span></li>
    </ul>
  </div>

  <div class="section section--light">
    <div class="ribbon">
      <svg viewBox="0 0 146 19" width="146" height="19"><polygon points="0,0 146,0 139,9.5 146,19 0,19 7,9.5" fill="#2a2526" stroke="#c9c08a" stroke-width="1"/></svg>
      <span class="ribbon__label">SOMETHING LIGHT</span>
    </div>
    <ul class="items items--left">
      <li><span class="name">Mixed Yoghurts</span><span class="price">$5.5</span></li>
      <li><span class="name">Granola and Fruit Yoghurt</span><span class="price">$5.5</span></li>
      <li><span class="name">Chia Pudding</span><span class="price">$5.5</span></li>
      <li><span class="name">Bircher Muesli</span><span class="price">$5.5</span></li>
      <li><span class="name">Fruit Salad</span><span class="price">$5.5</span></li>
      <li><span class="name">Banana Bread</span><span class="price">$4.5</span></li>
      <li><span class="name">Muffins – made fresh daily</span><span class="price">$4.5</span></li>
    </ul>
    <ul class="items items--right">
      <li><span class="name">Slices</span><span class="price">$4.0</span></li>
      <li><span class="name">Cookies</span><span class="price">$4.0</span></li>
      <li><span class="name">Choc Crunch Energy Bite</span><span class="price">$4.0</span></li>
      <li><span class="name">Super Crunch Energy Bite</span><span class="price">$4.0</span></li>
      <li><span class="name">Chocolate Bar</span><span class="price">$3.0</span></li>
      <li><span class="name">Packet of Chips</span><span class="price">$3.0</span></li>
    </ul>
  </div>
</section>

</body>
</html>
```